Business Card for a Life Coaching Company

BRAVOPEAK is a Life Coaching company that was initiated to support people who want to transform thier life or ana aspect of it.
our slogan is : "Aspire. Commit. Achieve"
our logo is uploaded.
The name of the company implies that leadership, strength and wisdom required to change your life.
We want an attractive business card that would give an impression of reliability, support and change. so we really want it unique. Here are some examples of unique cards:

http://www.cardcraftvault.example/2009/05/100-really-creative-business-cards/

BravoPeak is a life coaching organization focusing on individual transformation through the application of relevant and timeless principles of success.  BravoPeak believes that real, sustainable life transformations are brought about by tuning into the timeless wisdom we each carry in our hearts while boldy acting in the direction of our dreams.

Contacts on the card:
Address: 7 Tarek Nour El Dine Heliopolis Cairo Egypt
Tel: +202 24 71 38 52
Fax: +202 24 71 38 17
Mobile: +2 012 684 2097 (Dalia Soliman)
+2 0199915815 (Tariq Bhatti)

By the way, our temporary website is http://www.bravopeak.example

We have attached an .eps file with various configurations of our logo.

```html
<!DOCTYPE html>
<html lang="en">
<head>
<meta charset="utf-8">
<title>BravoPeak Business Card</title>
<link rel="stylesheet" href="https://fonts.googleapis.com/css2?family=Tinos&family=Lato:wght@400&display=swap">
<style>
  :root {
    --orange: #f47c20;
    --white: #ffffff;
    --ink-bg: #000000;
  }
  html, body {
    margin: 0;
    padding: 0;
    background: var(--ink-bg);
    overflow: hidden;
  }
  .sheet {
    position: relative;
    width: 1200px;
    height: 934px;
    background: var(--ink-bg);
    overflow: hidden;
  }
  .card {
    position: absolute;
  }
  .card svg.card-shape {
    position: absolute;
    left: 0;
    top: 0;
  }
  .card--front-light { left: 68px;  top: 83px;  width: 529px; height: 272px; }
  .card--back-light  { left: 634px; top: 76px;  width: 533px; height: 272px; }
  .card--front-dark  { left: 74px;  top: 486px; width: 534px; height: 309px; }
  .card--back-dark   { left: 634px; top: 483px; width: 531px; height: 299px; }

  .brand {
    position: absolute;
    font-family: "Tinos", "Times New Roman", serif;
    font-size: 52px;
    line-height: 50px;
    letter-spacing: 1px;
    white-space: nowrap;
  }
  .brand-dot {
    position: absolute;
    border-radius: 50%;
  }
  .slogan {
    position: absolute;
    font-family: "Tinos", "Times New Roman", serif;
    font-size: 25px;
    white-space: nowrap;
  }
  .contact {
    position: absolute;
    margin: 0;
    font-family: "Lato", "Gill Sans", sans-serif;
    font-size: 15px;
    line-height: 24px;
    white-space: nowrap;
  }
  .tone-orange { color: var(--orange); }
  .tone-white  { color: var(--white); }
  .fill-orange { background: var(--orange); }
  .fill-white  { background: var(--white); }
</style>
</head>
<body>
<main class="sheet">

  <!-- Front, white version -->
  <section class="card card--front-light">
    <svg class="card-shape" width="529" height="272" viewBox="0 0 529 272">
      <path d="M0 0H529V236C492 234 464 244 452 262C300 262 150 266 0 272Z" fill="var(--white)"/>
      <g fill="var(--orange)">
        <polygon points="0,22 98,54 98,76 0,44"/>
        <polygon points="0,70 98,102 98,124 0,92"/>
        <polygon points="0,118 98,150 98,172 0,140"/>
        <polygon points="0,166 98,198 98,220 0,188"/>
      </g>
    </svg>
    <span class="brand-dot fill-orange" style="left:152px; top:62px; width:72px; height:72px;"></span>
    <div class="brand tone-orange" style="left:236px; top:46px;">BRAVO<br>PEAK</div>
    <div class="slogan tone-orange" style="left:156px; top:178px;">Aspire. Commit. Achieve</div>
  </section>

  <!-- Back, white version -->
  <section class="card card--back-light">
    <svg class="card-shape" width="533" height="272" viewBox="0 0 533 272">
      <path d="M0 0H533V232C496 232 468 242 456 258C300 260 150 264 0 272Z" fill="var(--white)"/>
      <g fill="var(--orange)">
        <polygon points="0,24 94,56 94,78 0,46"/>
        <polygon points="0,72 94,104 94,126 0,94"/>
        <polygon points="0,120 94,152 94,174 0,142"/>
        <polygon points="0,168 94,200 94,222 0,190"/>
      </g>
    </svg>
    <p class="contact tone-orange" style="left:122px; top:70px;">
      7 Tarek Nour El Dine Heliopolis Cairo Egypt<br>
      Tel: +202 24 71 38 52<br>
      Fax: +202 24 71 38 17<br>
      Mobile: +2 012 684 2097 (Dalia Soliman)<br>
      +2 0197328406 (Tariq Bhatti)
    </p>
  </section>

  <!-- Front, orange version -->
  <section class="card card--front-dark">
    <svg class="card-shape" width="534" height="309" viewBox="0 0 534 309">
      <path d="M0 0H534V266C506 268 490 280 484 300C320 300 160 304 0 309Z" fill="var(--white)"/>
      <rect x="3" y="3" width="528" height="240" fill="var(--orange)"/>
      <g fill="var(--white)">
        <polygon points="3,40 94,72 94,94 3,62"/>
        <polygon points="3,88 94,120 94,142 3,110"/>
        <polygon points="3,136 94,168 94,190 3,158"/>
      </g>
      <rect x="3" y="243" width="528" height="6" fill="var(--white)"/>
      <rect x="3" y="249" width="528" height="10" fill="var(--orange)"/>
      <polygon points="3,259 531,259 531,262 500,262 478,280 3,280" fill="var(--white)"/>
      <polygon points="3,280 478,280 470,286 3,286" fill="var(--orange)"/>
    </svg>
    <span class="brand-dot fill-white" style="left:148px; top:68px; width:72px; height:72px;"></span>
    <div class="brand tone-white" style="left:232px; top:52px;">BRAVO<br>PEAK</div>
    <div class="slogan tone-white" style="left:160px; top:188px;">Aspire. Commit. Achieve</div>
  </section>

  <!-- Back, orange version -->
  <section class="card card--back-dark">
    <svg class="card-shape" width="531" height="299" viewBox="0 0 531 299">
      <path d="M0 0H531V256C504 258 488 270 482 290C320 292 160 294 0 299Z" fill="var(--white)"/>
      <rect x="3" y="3" width="525" height="232" fill="var(--orange)"/>
      <g fill="var(--white)">
        <polygon points="3,20 92,52 92,74 3,42"/>
        <polygon points="3,68 92,100 92,122 3,90"/>
        <polygon points="3,116 92,148 92,170 3,138"/>
      </g>
      <rect x="3" y="235" width="525" height="6" fill="var(--white)"/>
      <rect x="3" y="241" width="525" height="10" fill="var(--orange)"/>
      <polygon points="3,251 528,251 528,254 494,254 472,270 3,270" fill="var(--white)"/>
      <polygon points="3,270 472,270 464,276 3,276" fill="var(--orange)"/>
    </svg>
    <p class="contact tone-white" style="left:111px; top:80px;">
      7 Tarek Nour El Dine Heliopolis Cairo Egypt<br>
      Tel: +202 24 71 38 52<br>
      Fax: +202 24 71 38 17<br>
      Mobile: +2 012 684 2097 (Dalia Soliman)<br>
      +2 0197328406 (Tariq Bhatti)
    </p>
  </section>

</main>
</body>
</html>
```